100% Organic Beard Care Product labels

We need labels for our organic beard care products, this includes 30ml matt black bottles, 50ml matt black jars and 100ml matt black boston bottles.
We have six beard oil products, three beard balm products, and one beard shampoo.
Would like white on black, or white on transparent print and logo.
Logo is attached along with an idea of label for our unscented product.

Target Market(s)

Mens beard care

Other font styles liked:
• Verdana

```html
<!DOCTYPE html>
<html lang="en">
<head>
<meta charset="UTF-8">
<title>Guild of Gents – Beard Oil Label</title>
<link rel="stylesheet" href="https://fonts.googleapis.com/css2?family=Open+Sans:wght@400;600&family=Archivo+Black&display=swap">
<style>
  :root {
    --backdrop: #e1e1e1;
    --label-fill: #3a3a3a;
    --label-ink: #ffffff;
    --label-ink-soft: #e8e8e8;
    --rule: #f2f2f2;
  }
  * { box-sizing: border-box; margin: 0; padding: 0; }
  html, body {
    width: 1200px;
    height: 900px;
    overflow: hidden;
    background: var(--backdrop);
  }
  .canvas {
    width: 1200px;
    height: 900px;
    display: flex;
    align-items: center;
    justify-content: center;
  }
  .label {
    width: 420px;
    height: 740px;
    background: var(--label-fill);
    padding: 14px;
  }
  .label-frame {
    width: 100%;
    height: 100%;
    border: 3px solid var(--rule);
    display: flex;
    flex-direction: column;
    color: var(--label-ink);
    font-family: "Open Sans", Verdana, sans-serif;
  }
  .brand {
    flex: 0 0 52%;
    display: flex;
    flex-direction: column;
    align-items: center;
    justify-content: center;
    gap: 22px;
    border-bottom: 3px solid var(--rule);
  }
  .brand-dot {
    width: 64px;
    height: 64px;
    border-radius: 50%;
    background: var(--label-ink);
  }
  .brand-name {
    font-family: "Open Sans", Verdana, sans-serif;
    font-weight: 600;
    font-size: 44px;
    line-height: 1.05;
    text-align: center;
    text-transform: uppercase;
    letter-spacing: 1px;
    color: var(--label-ink);
  }
  .product {
    flex: 0 0 28%;
    display: flex;
    flex-direction: column;
    align-items: center;
    justify-content: center;
    gap: 14px;
    border-bottom: 3px solid var(--rule);
  }
  .product-name {
    font-weight: 400;
    font-size: 50px;
    letter-spacing: 1px;
    line-height: 1;
  }
  .moustache-mark {
    width: 130px;
    height: 38px;
    background: var(--label-ink-soft);
    border-radius: 50% 50% 40% 40% / 60% 60% 40% 40%;
  }
  .organic-claim {
    font-family: "Archivo Black", Verdana, sans-serif;
    font-size: 28px;
    letter-spacing: 1px;
    line-height: 1;
  }
  .variant {
    flex: 1;
    display: flex;
    flex-direction: column;
    align-items: center;
    justify-content: center;
    font-size: 32px;
    line-height: 1.3;
    color: var(--label-ink-soft);
  }
</style>
</head>
<body>
  <main class="canvas">
    <section class="label">
      <div class="label-frame">
        <header class="brand">
          <span class="brand-dot"></span>
          <p class="brand-name">Guild<br>of Gents</p>
        </header>
        <div class="product">
          <h1 class="product-name">BEARD OIL</h1>
          <div class="moustache-mark" role="img" aria-label="White moustache illustration"></div>
          <p class="organic-claim">100% ORGANIC</p>
        </div>
        <footer class="variant">
          <span class="variant-scent">unscented</span>
          <span class="variant-volume">30ml</span>
        </footer>
      </div>
    </section>
  </main>
</body>
</html>
```